Torvane PowerPoint Template

I have a company called Torvane, LLC and my company logo is already designed. I need a PowerPoint template that I will be using to pitch potential investors and business partners. This should be a very professional-looking template that leverages the company logo colors and really pops. The company is an AI product research and development company.

```html
<!DOCTYPE html>
<html lang="en">
<head>
<meta charset="utf-8">
<title>Torvane Presentation Template</title>
<link rel="stylesheet" href="https://fonts.googleapis.com/css2?family=Poppins:wght@400;500;600;700;800&display=swap">
<style>
:root{
  --red:#c4262e;
  --red-dark:#9e1b22;
  --ink:#3a3a3b;
  --grey:#c4c4c4;
  --soft:#f1f1f1;
  --text:#666;
  --bg:#ebebec;
  --white:#fff;
}
*{box-sizing:border-box;margin:0;padding:0}
html,body{width:1195px;height:1200px;overflow:hidden}
body{background:var(--bg);font-family:"Poppins",sans-serif;color:var(--ink);position:relative}
.slide{position:absolute;width:348px;height:196px;background:var(--white);overflow:hidden;box-shadow:0 2px 6px rgba(0,0,0,.12)}
.abs{position:absolute}
.kicker{position:absolute;font-size:10.5px;font-weight:500;line-height:1;color:var(--ink);text-transform:uppercase}
.headline{position:absolute;font-size:14px;font-weight:800;line-height:1;color:var(--red);text-transform:uppercase}
.copy{position:absolute;font-size:3.7px;line-height:1.55;color:var(--text)}
.photo{position:absolute}
.foot{position:absolute;left:5px;right:8px;top:183px;height:8px;display:flex;align-items:center}
.foot .brand{font-size:4.6px;font-weight:700;color:var(--red);display:flex;align-items:center;gap:1.5px}
.foot .brand i{display:block;width:5px;height:5px;border-radius:50%;background:var(--red)}
.foot .rule{flex:1;height:.7px;background:var(--red);margin:0 3px}
.foot .pg{font-size:3.6px;color:var(--ink)}
.item-title{font-size:5.5px;font-weight:700;color:var(--ink);line-height:1.2}
.red-title{font-size:5.4px;font-weight:600;color:var(--red);line-height:1.2}
.tiny{font-size:3.2px;line-height:1.5;color:var(--text)}
svg text{font-family:"Poppins",sans-serif}
</style>
</head>
<body>

<!-- 1 Cover -->
<section class="slide" style="left:54px;top:64px">
  <div class="abs" style="left:22px;top:21px;display:flex;align-items:center;gap:4px">
    <span style="width:19px;height:19px;border-radius:50%;background:var(--red);display:block"></span>
    <span style="font-size:17px;font-weight:600;color:var(--red);letter-spacing:-.3px">Torvane</span>
  </div>
  <div class="photo" role="img" aria-label="Glowing AI brain network held between robotic hands" style="left:143px;top:22px;width:205px;height:152px;background:radial-gradient(circle at 55% 40%,#4fb3ff 0,#1c5ea8 22%,#0c2547 55%,#060f1f 100%)"></div>
  <div class="abs" style="left:0;top:54px;width:197px;height:98px;background:var(--red);border-radius:0 20px 20px 0"></div>
  <div class="abs" style="left:22px;top:74px;font-size:22px;font-weight:800;color:var(--white);line-height:1">BUSINESS</div>
  <div class="abs" style="left:22px;top:101px;font-size:7.4px;font-weight:600;color:var(--white)">Presentation Template</div>
  <div class="abs" style="left:22px;top:116px;font-size:3.8px;line-height:1.55;color:var(--white)">Lorem ipsum is simply dummy text<br>of the printing and typesetting industry.</div>
  <svg class="abs" style="left:156px;top:64px" width="28" height="78" viewBox="0 0 28 78">
    <g fill="#fff"><circle cx="2" cy="2" r=".7"/><circle cx="8" cy="2" r=".7"/><circle cx="14" cy="2" r=".7"/><circle cx="14" cy="8" r=".7"/><circle cx="14" cy="14" r=".7"/><circle cx="14" cy="60" r=".7"/><circle cx="14" cy="66" r=".7"/><circle cx="14" cy="72" r=".7"/><circle cx="8" cy="72" r=".7"/><circle cx="2" cy="72" r=".7"/></g>
  </svg>
  <div class="abs" style="left:22px;top:164px;display:flex;align-items:center;gap:3px;font-size:5px;color:var(--ink)">
    <span style="width:11px;height:11px;border-radius:50%;background:var(--red);display:block"></span>Your Website Name Goes Here
  </div>
</section>

<!-- 2 Table of content -->
<section class="slide" style="left:425px;top:64px">
  <div class="kicker" style="left:36px;top:74px">Table of</div>
  <div class="headline" style="left:36px;top:86px;font-size:17px">Content</div>
  <p class="copy" style="left:36px;top:106px;width:132px">Lorem Ipsum is simply dummy text of the printing and typesetting industry. Lorem Ipsum has been the industry's standard dummy text ever since the 1500s.</p>
  <svg class="abs" style="left:0;top:0" width="348" height="196" viewBox="0 0 348 196">
    <g font-size="4" fill="#3a3a3b">
      <g transform="translate(0,46)"><circle cx="181" cy="0" r="1" fill="#c4262e"/><text x="185" y="1.4">Simple Text One</text><line x1="185" y1="4" x2="300" y2="4" stroke="#c4262e" stroke-width=".4"/><circle cx="304" cy="4" r="4.5"/><text x="304" y="5.4" fill="#fff" font-size="3.6" text-anchor="middle">02</text></g>
      <g transform="translate(0,65)"><circle cx="181" cy="0" r="1" fill="#c4262e"/><text x="185" y="1.4">Simple Text Two</text><line x1="185" y1="4" x2="300" y2="4" stroke="#c4262e" stroke-width=".4"/><circle cx="304" cy="4" r="4.5"/><text x="304" y="5.4" fill="#fff" font-size="3.6" text-anchor="middle">04</text></g>
      <g transform="translate(0,84)"><circle cx="181" cy="0" r="1" fill="#c4262e"/><text x="185" y="1.4">Simple Text Three</text><line x1="185" y1="4" x2="300" y2="4" stroke="#c4262e" stroke-width=".4"/><circle cx="304" cy="4" r="4.5"/><text x="304" y="5.4" fill="#fff" font-size="3.6" text-anchor="middle">06</text></g>
      <g transform="translate(0,103)"><circle cx="181" cy="0" r="1" fill="#c4262e"/><text x="185" y="1.4">Simple Text Four</text><line x1="185" y1="4" x2="300" y2="4" stroke="#c4262e" stroke-width=".4"/><circle cx="304" cy="4" r="4.5"/><text x="304" y="5.4" fill="#fff" font-size="3.6" text-anchor="middle">08</text></g>
      <g transform="translate(0,122)"><circle cx="181" cy="0" r="1" fill="#c4262e"/><text x="185" y="1.4">Simple Text Five</text><line x1="185" y1="4" x2="300" y2="4" stroke="#c4262e" stroke-width=".4"/><circle cx="304" cy="4" r="4.5"/><text x="304" y="5.4" fill="#fff" font-size="3.6" text-anchor="middle">10</text></g>
      <g transform="translate(0,141)"><circle cx="181" cy="0" r="1" fill="#c4262e"/><text x="185" y="1.4">Simple Text Six</text><line x1="185" y1="4" x2="300" y2="4" stroke="#c4262e" stroke-width=".4"/><circle cx="304" cy="4" r="4.5"/><text x="304" y="5.4" fill="#fff" font-size="3.6" text-anchor="middle">12</text></g>
    </g>
  </svg>
  <div class="foot"><span class="brand"><i></i>Torvane</span><b class="rule"></b><span class="pg">2</span></div>
</section>

<!-- 3 Products and services -->
<section class="slide" style="left:792px;top:64px">
  <div class="kicker" style="left:15px;top:20px">Products</div>
  <div class="headline" style="left:15px;top:33px">And Services</div>
  <svg class="abs" style="left:30px;top:62px" width="22" height="90" viewBox="0 0 22 90" fill="none" stroke="#c4262e" stroke-width="1.3">
    <path d="M5 12a5 5 0 0 1 1-9 6 6 0 0 1 11 2 4 4 0 0 1 0 7"/><path d="M12 7l-3 5h4l-3 5"/>
    <circle cx="11" cy="42" r="4"/><circle cx="11" cy="42" r="1.5" fill="#c4262e"/><path d="M11 35v3M11 46v3M4 42h3M15 42h3"/>
    <rect x="3" y="68" width="16" height="12" rx="1"/><path d="M7 77v-4M11 77v-6M15 77v-3M8 83h6"/>
  </svg>
  <div class="abs" style="left:56px;top:63px;width:120px"><div class="item-title">Lorem ipsum dolor.</div><p class="tiny">Lorem ipsumectetuer adipiscing elit, sed diam nonummy nibh euismod tincidunt</p></div>
  <div class="abs" style="left:56px;top:99px;width:120px"><div class="item-title">Lorem ipsum dolor.</div><p class="tiny">Lorem ipsumectetuer adipiscing elit, sed diam nonummy nibh euismod tincidunt</p></div>
  <div class="abs" style="left:56px;top:135px;width:120px"><div class="item-title">Lorem ipsum dolor.</div><p class="tiny">Lorem ipsumectetuer adipiscing elit, sed diam nonummy nibh euismod tincidunt</p></div>
  <div class="photo" role="img" aria-label="Hands typing on a laptop with a glowing holographic robot" style="left:181px;top:27px;width:138px;height:145px;border-radius:16px;background:linear-gradient(150deg,#0e3c4a 0,#1d8c98 45%,#0a2a35 100%)"></div>
  <div class="foot"><span class="brand"><i></i>Torvane</span><b class="rule"></b><span class="pg">3</span></div>
</section>

<!-- 4 Report content summary -->
<section class="slide" style="left:54px;top:285px">
  <div class="kicker" style="left:11px;top:14px">Report</div>
  <div class="headline" style="left:11px;top:27px">Content Summary</div>
  <div class="abs" style="left:22px;top:53px;width:145px">
    <div class="red-title">01. Aliquam Erat Volutpat</div>
    <p class="tiny" style="margin-top:2px">Lorem ipsum dolor sit amet, consectetuer adipiscing elit, sed diamnonummy nibh euismod</p>
    <p class="tiny" style="margin-top:4px">Lorem ipsum dolor sit amet, cons ectetuer adipiscing elit, sed diamnonummy nibh euismod tincidunt ut laoreet sed diam cons ectetuer adipiscing elit</p>
    <div class="red-title" style="margin-top:8px">02. Consectetuer Adipiscing Elit</div>
    <p class="tiny" style="margin-top:2px">Lorem ipsum dolor sit amet, consectetuer adipiscing elit, sed diamnonummy nibh euismod</p>
    <p class="tiny" style="margin-top:4px">Lorem ipsum dolor sit amet, cons ectetuer adipiscing elit, sed diamnonummy nibh euismod tincidunt ut laoreet sed diam cons ectetuer adipiscing elit</p>
  </div>
  <div class="abs" style="left:188px;top:53px;width:140px">
    <div class="red-title">03. Aliquam Erat Volutpat</div>
    <p class="tiny" style="margin-top:2px">Lorem ipsum dolor sit amet, consectetuer adipiscing elit, sed diam nonummy nibh euismod</p>
    <p class="tiny" style="margin-top:4px">Lorem ipsum dolor sit amet, cons ectetuer adipiscing elit, sed diam nonummy nibh cons ectetuer adipiscing elit</p>
    <div style="margin-top:5px;font-size:3.6px;font-weight:600;color:var(--red)">● Lorem ipsum dolor</div>
    <p class="tiny" style="font-size:2.6px;padding-left:4px">Lorem ipsum dolor sit amet, consectetuer adipiscing elit, sed diam nonummy nibh euismod tincidunt ut laoreet</p>
    <div style="margin-top:4px;font-size:3.6px;font-weight:600;color:var(--red)">● Lorem ipsum dolor</div>
    <p class="tiny" style="font-size:2.6px;padding-left:4px">Lorem ipsum dolor sit amet, consectetuer adipiscing elit sed diam nonummy nibh euismod tincidunt ut laoreet</p>
    <div style="margin-top:4px;font-size:3.6px;font-weight:600;color:var(--red)">● Lorem ipsum dolor</div>
    <p class="tiny" style="font-size:2.6px;padding-left:4px">Lorem ipsum dolor sit amet, consectetuer adipiscing elit, sed diam nonummy nibh euismod tincidunt ut laoreet</p>
  </div>
  <div class="foot"><span class="brand"><i></i>Torvane</span><b class="rule"></b><span class="pg">4</span></div>
</section>

<!-- 5 Section divider -->
<section class="slide" style="left:425px;top:285px">
  <div class="photo" role="img" aria-label="Red-tinted photo of hands at a laptop with data overlay" style="left:0;top:19px;width:348px;height:156px;background:radial-gradient(circle at 35% 40%,#d9474d 0,#c4262e 45%,#b21f27 100%)"></div>
  <div class="abs" style="left:88px;top:78px;font-size:38px;font-weight:800;color:var(--white);line-height:1">01.</div>
  <div class="abs" style="left:147px;top:80px;font-size:17px;font-weight:600;color:var(--white);line-height:1">Part One.</div>
  <div class="abs" style="left:147px;top:102px;font-size:5.6px;line-height:1.5;color:var(--white)">Lorem ipsumectetuer adipiscing elit<br>sed diam nonummy nibh euismod tincidunt</div>
  <div class="abs" style="left:295px;top:157px;display:flex;align-items:center;gap:2px;font-size:7px;font-weight:600;color:var(--white)"><span style="width:9px;height:9px;border-radius:50%;background:var(--white);display:block"></span>Torvane</div>
</section>

<!-- 6 Mission and vision -->
<section class="slide" style="left:792px;top:285px">
  <div class="kicker" style="left:25px;top:20px">Company</div>
  <div class="headline" style="left:25px;top:33px">Mission &amp; Vision</div>
  <p class="copy" style="left:25px;top:50px;width:135px">Lorem ipsum dolor sit amet, cons ectetuer adipiscing elit, sed diam nonummy nibh euismod tincidunt.Lorem ipsum dolor sit amet.</p>
  <div class="photo" role="img" aria-label="Team presenting in a control room full of screens" style="left:25px;top:80px;width:131px;height:76px;border-radius:6px;background:linear-gradient(160deg,#2c5c8f 0,#173556 55%,#0d1e33 100%)"></div>
  <div class="abs" style="left:169px;top:45px;width:155px;height:50px;border-radius:8px;background:var(--soft)"></div>
  <div class="abs" style="left:169px;top:45px;width:37px;height:50px;border-radius:8px;background:var(--red)"></div>
  <svg class="abs" style="left:179px;top:60px" width="18" height="20" viewBox="0 0 18 20" fill="none" stroke="#fff" stroke-width="1.2"><path d="M3 10l9-6v12z"/><path d="M3 8v4M6 14l1 4"/><path d="M15 5l2-2M15 10h3M15 15l2 2"/></svg>
  <div class="abs" style="left:214px;top:51px;width:104px"><div class="item-title" style="font-size:7px">Mission</div><p class="tiny" style="margin-top:2px;line-height:1.9">Lorem ipsum dolor sit amet, cons ectetuer adipiscing elit, sed diam nonummy nibh euismod tincidunt.</p></div>
  <div class="abs" style="left:169px;top:106px;width:155px;height:50px;border-radius:8px;background:var(--soft)"></div>
  <div class="abs" style="left:169px;top:106px;width:37px;height:50px;border-radius:8px;background:var(--red)"></div>
  <svg class="abs" style="left:179px;top:121px" width="18" height="20" viewBox="0 0 18 20" fill="none" stroke="#fff" stroke-width="1.2"><path d="M3 3l12 14M15 3L3 17"/><path d="M2 16l2 2M14 2l2 2"/></svg>
  <div class="abs" style="left:214px;top:112px;width:104px"><div class="item-title" style="font-size:7px">Vision</div><p class="tiny" style="margin-top:2px;line-height:1.9">Lorem ipsum dolor sit amet, cons ectetuer adipiscing elit, sed diam nonummy nibh euismod tincidunt.</p></div>
  <div class="foot"><span class="brand"><i></i>Torvane</span><b class="rule"></b><span class="pg">6</span></div>
</section>

<!-- 7 Summary report -->
<section class="slide" style="left:54px;top:506px">
  <div class="kicker" style="left:15px;top:11px">Our Company</div>
  <div class="headline" style="left:15px;top:22px">Summary Report</div>
  <svg class="abs" style="left:0;top:0" width="348" height="196" viewBox="0 0 348 196">
    <text x="116" y="55" font-size="6" fill="#3a3a3b" text-anchor="middle">Chart Title</text>
    <g font-size="2.8" fill="#666"><rect x="87" y="60" width="2" height="2" fill="#c4262e"/><text x="90" y="62">Series 3</text><rect x="107" y="60" width="2" height="2" fill="#3a3a3b"/><text x="110" y="62">Series 2</text><rect x="127" y="60" width="2" height="2" fill="#c4c4c4"/><text x="130" y="62">Series 1</text></g>
    <g font-size="3" fill="#555">
      <text x="48" y="82" text-anchor="end">Category 4</text>
      <rect x="52" y="75" width="125" height="3.6" fill="#c4262e"/><rect x="52" y="80" width="70" height="3.6" fill="#3a3a3b"/><rect x="52" y="85" width="112" height="3.6" fill="#c4c4c4"/>
      <text x="179" y="78">5</text><text x="124" y="83">2.8</text><text x="166" y="88">4.5</text>
      <text x="48" y="106" text-anchor="end">Category 3</text>
      <rect x="52" y="99" width="75" height="3.6" fill="#c4262e"/><rect x="52" y="104" width="45" height="3.6" fill="#3a3a3b"/><rect x="52" y="109" width="87" height="3.6" fill="#c4c4c4"/>
      <text x="129" y="102">3</text><text x="99" y="107">1.8</text><text x="141" y="112">3.5</text>
      <text x="48" y="129" text-anchor="end">Category 2</text>
      <rect x="52" y="122" width="50" height="3.6" fill="#c4262e"/><rect x="52" y="127" width="110" height="3.6" fill="#3a3a3b"/><rect x="52" y="132" width="62" height="3.6" fill="#c4c4c4"/>
      <text x="104" y="125">2</text><text x="164" y="130">4.4</text><text x="116" y="135">2.5</text>
      <text x="48" y="151" text-anchor="end">Category 1</text>
      <rect x="52" y="144" width="50" height="3.6" fill="#c4262e"/><rect x="52" y="149" width="60" height="3.6" fill="#3a3a3b"/><rect x="52" y="154" width="107" height="3.6" fill="#c4c4c4"/>
      <text x="104" y="147">2</text><text x="114" y="152">2.4</text><text x="161" y="157">4.3</text>
    </g>
    <text x="258" y="42" font-size="5.5" fill="#3a3a3b" text-anchor="middle">SALES</text>
    <g font-size="2.8" fill="#666"><rect x="227" y="48" width="2" height="2" fill="#c4262e"/><text x="230" y="50">1st Qtr</text><rect x="248" y="48" width="2" height="2" fill="#3a3a3b"/><text x="251" y="50">2nd Qtr</text><rect x="269" y="48" width="2" height="2" fill="#c4c4c4"/><text x="272" y="50">3rd Qtr</text></g>
    <g transform="rotate(-90 258 117)" fill="none" stroke-width="26">
      <circle cx="258" cy="117" r="37" stroke="#c4262e" stroke-dasharray="148.8 232.5"/>
      <circle cx="258" cy="117" r="37" stroke="#3a3a3b" stroke-dasharray="58.1 232.5" stroke-dashoffset="-148.8"/>
      <circle cx="258" cy="117" r="37" stroke="#c4c4c4" stroke-dasharray="25.6 232.5" stroke-dashoffset="-206.9"/>
    </g>
    <g font-size="3.4" fill="#fff"><text x="288" y="134">64%</text><text x="216" y="113">25%</text><text x="242" y="87">11%</text></g>
  </svg>
  <div class="foot"><span class="brand"><i></i>Torvane</span><b class="rule"></b><span class="pg">7</span></div>
</section>

<!-- 8 Report analytics -->
<section class="slide" style="left:425px;top:506px">
  <div class="kicker" style="left:21px;top:25px;font-size:9.5px">Our Company</div>
  <div class="headline" style="left:21px;top:36px;font-size:13.5px">Report Analytics</div>
  <p class="copy" style="left:21px;top:58px;width:140px">Lorem ipsum dolor amet consectetur adipisc eiusmod incididunt labore dolore magna ullamco aliqua. Aliquip commodo consequat.</p>
  <svg class="abs" style="left:0;top:0" width="348" height="196" viewBox="0 0 348 196">
    <text x="250" y="27" font-size="4.4" fill="#555" text-anchor="middle">Chart Title</text>
    <g stroke="#e2e2e2" stroke-width=".3"><line x1="187" y1="34" x2="314" y2="34"/><line x1="187" y1="41" x2="314" y2="41"/><line x1="187" y1="47" x2="314" y2="47"/><line x1="187" y1="54" x2="314" y2="54"/><line x1="187" y1="60" x2="314" y2="60"/><line x1="187" y1="67" x2="314" y2="67"/><line x1="187" y1="73" x2="314" y2="73"/></g>
    <g font-size="2.6" fill="#777"><text x="183" y="35">6</text><text x="183" y="48">4</text><text x="183" y="61">2</text><text x="183" y="74">0</text>
      <text x="196" y="78">Category 1</text><text x="228" y="78">Category 2</text><text x="260" y="78">Category 3</text><text x="292" y="78">Category 4</text></g>
    <polyline points="203,58 219,50 235,50 251,61 267,58 298,56" fill="none" stroke="#c4262e" stroke-width=".9"/>
    <polyline points="203,52 219,59 235,57 251,58 267,53 298,46" fill="none" stroke="#3a3a3b" stroke-width=".9"/>
    <polyline points="203,62 235,61 251,58 267,55 298,48" fill="none" stroke="#c4c4c4" stroke-width=".9"/>
    <g font-size="2.6" fill="#777"><line x1="217" y1="83" x2="223" y2="83" stroke="#c4262e"/><text x="224" y="84">Series 1</text><line x1="240" y1="83" x2="246" y2="83" stroke="#3a3a3b"/><text x="247" y="84">Series 2</text><line x1="263" y1="83" x2="269" y2="83" stroke="#c4c4c4"/><text x="270" y="84">Series 3</text></g>

    <text x="130" y="107" font-size="4.6" fill="#3a3a3b" text-anchor="middle">Chart Title</text>
    <g stroke="#e6e6e6" stroke-width=".3"><line x1="29" y1="113" x2="230" y2="113"/><line x1="29" y1="126" x2="230" y2="126"/><line x1="29" y1="138" x2="230" y2="138"/><line x1="29" y1="151" x2="230" y2="151"/></g>
    <g font-size="2.6" fill="#777"><text x="25" y="114">6</text><text x="25" y="127">4</text><text x="25" y="139">2</text><text x="25" y="152">0</text></g>
    <g>
      <rect x="38" y="124" width="10" height="27" fill="#c4262e"/><rect x="50" y="136" width="10" height="15" fill="#3a3a3b"/><rect x="62" y="138.5" width="10" height="12.5" fill="#c4c4c4"/>
      <rect x="88" y="135.5" width="10" height="15.5" fill="#c4262e"/><rect x="100" y="123.5" width="10" height="27.5" fill="#3a3a3b"/><rect x="112" y="138.5" width="10" height="12.5" fill="#c4c4c4"/>
      <rect x="138" y="129" width="10" height="22" fill="#c4262e"/><rect x="150" y="140" width="10" height="11" fill="#3a3a3b"/><rect x="162" y="132" width="10" height="19" fill="#c4c4c4"/>
      <rect x="188" y="123" width="10" height="28" fill="#c4262e"/><rect x="200" y="133.5" width="10" height="17.5" fill="#3a3a3b"/><rect x="212" y="119.5" width="10" height="31.5" fill="#c4c4c4"/>
    </g>
    <g font-size="2.6" fill="#555"><text x="40" y="122">4.3</text><text x="52" y="134">2.4</text><text x="66" y="136">2</text><text x="90" y="133">2.5</text><text x="102" y="121">4.4</text><text x="116" y="136">2</text><text x="140" y="127">3.5</text><text x="152" y="138">1.8</text><text x="166" y="130">3</text><text x="190" y="121">4.5</text><text x="202" y="131">2.8</text><text x="216" y="117">5</text>
      <text x="43" y="157">Category 1</text><text x="93" y="157">Category 2</text><text x="143" y="157">Category 3</text><text x="193" y="157">Category 4</text></g>
    <g font-size="2.6" fill="#777"><rect x="102" y="160" width="2" height="2" fill="#c4262e"/><text x="105" y="162">Series 1</text><rect x="122" y="160" width="2" height="2" fill="#3a3a3b"/><text x="125" y="162">Series 2</text><rect x="142" y="160" width="2" height="2" fill="#c4c4c4"/><text x="145" y="162">Series 3</text></g>

    <text x="285" y="112" font-size="4.4" fill="#555" text-anchor="middle">Sales</text>
    <ellipse cx="283" cy="134" rx="32" ry="13" fill="#2a2a2b"/>
    <rect x="251" y="128" width="64" height="6" fill="#2a2a2b"/>
    <path d="M283 128 L300 120 A32 13 0 0 1 311 136 L303 138 Z" fill="#7a1218"/>
    <ellipse cx="283" cy="128" rx="32" ry="13" fill="#444"/>
    <path d="M283 128 L300 116.5 A32 13 0 0 1 305 137 Z" fill="#c4262e"/>
    <path d="M283 128 L305 137 A32 13 0 0 1 275 140.6 Z" fill="#c4c4c4"/>
    <g font-size="2.6" fill="#777"><rect x="266" y="160" width="2" height="2" fill="#3a3a3b"/><text x="269" y="162">1st Qtr</text><rect x="283" y="160" width="2" height="2" fill="#c4262e"/><text x="286" y="162">2nd Qtr</text><rect x="300" y="160" width="2" height="2" fill="#c4c4c4"/><text x="303" y="162">3rd Qtr</text></g>
  </svg>
  <div class="foot"><span class="brand"><i></i>Torvane</span><b class="rule"></b><span class="pg">8</span></div>
</section>

<!-- 9 Monthly chart -->
<section class="slide" style="left:792px;top:506px">
  <div class="kicker" style="left:21px;top:27px">Our Company</div>
  <div class="headline" style="left:21px;top:39px;font-size:15px">Monthly Chart</div>
  <svg class="abs" style="left:33px;top:73px" width="20" height="80" viewBox="0 0 20 80">
    <circle cx="9" cy="9" r="9" fill="#c4262e"/><text x="9" y="12" font-size="8" font-weight="700" fill="#fff" text-anchor="middle">1</text>
    <circle cx="9" cy="40" r="9" fill="#3a3a3b"/><text x="9" y="43" font-size="8" font-weight="700" fill="#fff" text-anchor="middle">2</text>
    <circle cx="9" cy="71" r="9" fill="#c4c4c4"/><text x="9" y="74" font-size="8" font-weight="700" fill="#fff" text-anchor="middle">3</text>
  </svg>
  <div class="abs" style="left:62px;top:74px;width:105px"><div class="item-title" style="font-size:5px">Lorem ipsum dolor.</div><p class="tiny" style="font-size:3.5px">Lorem ipsumectetuer adipiscing elit, sed diam nonummy nibh euismod tincidunt</p></div>
  <div class="abs" style="left:62px;top:105px;width:105px"><div class="item-title" style="font-size:5px">Lorem ipsum dolor.</div><p class="tiny" style="font-size:3.5px">Lorem ipsumectetuer adipiscing elit, sed diam nonummy nibh euismod tincidunt</p></div>
  <div class="abs" style="left:62px;top:136px;width:105px"><div class="item-title" style="font-size:5px">Lorem ipsum dolor.</div><p class="tiny" style="font-size:3.5px">Lorem ipsumectetuer adipiscing elit, sed diam nonummy nibh euismod tincidunt</p></div>
  <svg class="abs" style="left:0;top:0" width="348" height="196" viewBox="0 0 348 196">
    <g stroke="#e6e6e6" stroke-width=".3"><line x1="186" y1="39" x2="328" y2="39"/><line x1="186" y1="55" x2="328" y2="55"/><line x1="186" y1="71" x2="328" y2="71"/><line x1="186" y1="87" x2="328" y2="87"/><line x1="186" y1="104" x2="328" y2="104"/><line x1="186" y1="120" x2="328" y2="120"/><line x1="186" y1="136" x2="328" y2="136"/><line x1="186" y1="152" x2="328" y2="152"/></g>
    <g font-size="2.4" fill="#777"><text x="181" y="40">7</text><text x="181" y="56">6</text><text x="181" y="72">5</text><text x="181" y="88">4</text><text x="181" y="105">3</text><text x="181" y="121">2</text><text x="181" y="137">1</text><text x="181" y="153">0</text></g>
    <rect x="196" y="62" width="8" height="90" fill="#c4262e"/><rect x="206" y="76" width="8" height="76" fill="#3a3a3b"/><rect x="216" y="97" width="8" height="55" fill="#c4c4c4"/>
    <rect x="242" y="62" width="8" height="90" fill="#c4262e"/><rect x="252" y="44" width="8" height="108" fill="#3a3a3b"/><rect x="262" y="83" width="8" height="69" fill="#c4c4c4"/>
    <rect x="289" y="57" width="8" height="95" fill="#c4262e"/><rect x="299" y="96" width="8" height="56" fill="#3a3a3b"/><rect x="309" y="83" width="8" height="69" fill="#c4c4c4"/>
    <g font-size="3.4" fill="#555" text-anchor="middle"><text x="210" y="159">Category 1</text><text x="256" y="159">Category 1</text><text x="303" y="159">Category 1</text></g>
    <g font-size="2.4" fill="#777"><rect x="230" y="164" width="1.6" height="1.6" fill="#3a3a3b"/><text x="233" y="165.6">Series 1</text><rect x="249" y="164" width="1.6" height="1.6" fill="#c4262e"/><text x="252" y="165.6">Series 1</text><rect x="268" y="164" width="1.6" height="1.6" fill="#c4c4c4"/><text x="271" y="165.6">Series 1</text></g>
  </svg>
  <div class="foot"><span class="brand"><i></i>Torvane</span><b class="rule"></b><span class="pg">9</span></div>
</section>

<!-- 10 About our company -->
<section class="slide" style="left:54px;top:724px">
  <svg class="abs" style="left:0;top:0" width="348" height="196" viewBox="0 0 348 196">
    <polygon points="166,0 176,0 227,106 217,106" fill="#c4262e"/>
  </svg>
  <div class="photo" role="img" aria-label="Hands using a laptop under a holographic technology interface" style="left:176px;top:0;width:172px;height:106px;clip-path:polygon(0 0,100% 0,100% 100%,30% 100%);background:linear-gradient(135deg,#6b6258 0,#3b342e 50%,#1f1b18 100%)"></div>
  <div class="abs" style="left:25px;top:24px;font-size:4.8px;font-weight:500;color:var(--ink)">A BUSINESS TEXT HERE</div>
  <div class="headline" style="left:25px;top:32px;font-size:17px">About Our</div>
  <div class="abs" style="left:25px;top:50px;font-size:13px;font-weight:700;color:var(--ink);line-height:1">COMPANY</div>
  <p class="copy" style="left:25px;top:69px;width:135px;font-size:3.9px">Lorem ipsum dolor amet consectetur adipisc eiusmod incididunt labore dolore magna ullamco aliqua. Aliquip commodo consequat.</p>
  <svg class="abs" style="left:25px;top:107px" width="12" height="60" viewBox="0 0 12 60">
    <g><circle cx="6" cy="5" r="5" fill="#c4262e"/><path d="M3.5 5l2 2 3-3.5" stroke="#fff" stroke-width="1" fill="none"/></g>
    <g transform="translate(0,21)"><circle cx="6" cy="5" r="5" fill="#c4262e"/><path d="M3.5 5l2 2 3-3.5" stroke="#fff" stroke-width="1" fill="none"/></g>
    <g transform="translate(0,42)"><circle cx="6" cy="5" r="5" fill="#c4262e"/><path d="M3.5 5l2 2 3-3.5" stroke="#fff" stroke-width="1" fill="none"/></g>
  </svg>
  <p class="copy" style="left:43px;top:107px;width:105px">Lorem Ipsum is simply dummy text ofn the print and typeseting magna aliqua.</p>
  <p class="copy" style="left:43px;top:128px;width:105px">Lorem Ipsum is simply dummy text ofn the print and typeseting magna aliqua.</p>
  <p class="copy" style="left:43px;top:149px;width:105px">Lorem Ipsum is simply dummy text ofn the print and typeseting magna aliqua.</p>
  <svg class="abs" style="left:169px;top:120px" width="14" height="14" viewBox="0 0 14 14"><polygon points="7,0 13,3.5 13,10.5 7,14 1,10.5 1,3.5" fill="#3a3a3b"/><circle cx="7" cy="7" r="2.5" fill="none" stroke="#fff" stroke-width=".8"/></svg>
  <div class="abs red-title" style="left:186px;top:124px;font-size:4.8px">Write Simple Text</div>
  <p class="copy" style="left:170px;top:138px;width:76px;font-size:3.4px">Lorem Ipsum is simply dummy text a print and typeset industry has text ever since the 1500s.</p>
  <svg class="abs" style="left:256px;top:120px" width="14" height="14" viewBox="0 0 14 14"><polygon points="7,0 13,3.5 13,10.5 7,14 1,10.5 1,3.5" fill="#3a3a3b"/><path d="M4 10c1-4 3-5 6-5M8 3l2 2-2 2" stroke="#fff" stroke-width=".9" fill="none"/></svg>
  <div class="abs red-title" style="left:273px;top:124px;font-size:4.8px">Write Simple Text</div>
  <p class="copy" style="left:257px;top:138px;width:76px;font-size:3.4px">Lorem Ipsum is simply dummy text a print and typeset industry has text ever since the 1500s.</p>
  <div class="foot"><span class="brand"><i></i>Torvane</span><b class="rule"></b><span class="pg">10</span></div>
</section>

<!-- 11 Market analysis -->
<section class="slide" style="left:425px;top:724px">
  <div class="kicker" style="left:14px;top:18px;font-size:9.5px">Market Analysis</div>
  <div class="headline" style="left:14px;top:29px;font-size:13.5px">For A Business Plan</div>
  <svg class="abs" style="left:0;top:0" width="348" height="196" viewBox="0 0 348 196">
    <g transform="rotate(-90 173 106)" fill="none" stroke-width="24">
      <circle cx="173" cy="106" r="36" stroke="#c4262e" stroke-dasharray="55.5 226.2"/>
      <circle cx="173" cy="106" r="36" stroke="#3a3a3b" stroke-dasharray="55.5 226.2" stroke-dashoffset="-56.5"/>
      <circle cx="173" cy="106" r="36" stroke="#c4262e" stroke-dasharray="55.5 226.2" stroke-dashoffset="-113.1"/>
      <circle cx="173" cy="106" r="36" stroke="#3a3a3b" stroke-dasharray="55.5 226.2" stroke-dashoffset="-169.6"/>
    </g>
    <g fill="#fff"><circle cx="173" cy="58" r="3"/><circle cx="221" cy="106" r="3"/><circle cx="173" cy="154" r="3"/><circle cx="125" cy="106" r="3"/></g>
    <g fill="none" stroke="#fff" stroke-width=".9"><circle cx="150" cy="82" r="4"/><circle cx="150" cy="82" r="1.5"/><path d="M194 87l5-6m-5 6l-2-2m2 2l2 2"/><circle cx="197" cy="130" r="4"/><rect x="146" y="126" width="8" height="7" rx="1"/></g>
    <text x="173" y="104" font-size="7.5" font-weight="700" fill="#3a3a3b" text-anchor="middle">Text</text>
    <text x="173" y="113" font-size="7.5" font-weight="700" fill="#3a3a3b" text-anchor="middle">Added</text>
    <g text-anchor="end"><text x="114" y="65" font-size="6" font-weight="600" fill="#3a3a3b">Text Here</text>
      <text x="114" y="70" font-size="2.9" fill="#777">Lorem ipsum dolor sit amet, consectetuer</text><text x="114" y="73.5" font-size="2.9" fill="#777">adipiscing elit, sed diammy nibh euismod</text><text x="114" y="77" font-size="2.9" fill="#777">tincidunt ut laoreet dolore</text>
      <text x="114" y="135" font-size="6" font-weight="600" fill="#3a3a3b">Text Here</text>
      <text x="114" y="140" font-size="2.9" fill="#777">Lorem ipsum dolor sit amet, consectetuer</text><text x="114" y="143.5" font-size="2.9" fill="#777">adipiscing elit, sed diammy nibh euismod</text><text x="114" y="147" font-size="2.9" fill="#777">tincidunt ut laoreet dolore</text></g>
    <g><text x="233" y="65" font-size="6" font-weight="600" fill="#3a3a3b">Text Here</text>
      <text x="233" y="70" font-size="2.9" fill="#777">Lorem ipsum dolor sit amet, consectetuer</text><text x="233" y="73.5" font-size="2.9" fill="#777">adipiscing elit, sed diammy nibh euismod</text><text x="233" y="77" font-size="2.9" fill="#777">tincidunt ut laoreet dolore</text>
      <text x="233" y="135" font-size="6" font-weight="600" fill="#3a3a3b">Text Here</text>
      <text x="233" y="140" font-size="2.9" fill="#777">Lorem ipsum dolor sit amet, consectetuer</text><text x="233" y="143.5" font-size="2.9" fill="#777">adipiscing elit, sed diammy nibh euismod</text><text x="233" y="147" font-size="2.9" fill="#777">tincidunt ut laoreet dolore</text></g>
  </svg>
  <div class="foot"><span class="brand"><i></i>Torvane</span><b class="rule"></b><span class="pg">11</span></div>
</section>

<!-- 12 Text and table -->
<section class="slide" style="left:792px;top:724px">
  <div class="kicker" style="left:18px;top:24px">Text</div>
  <div class="headline" style="left:18px;top:36px">Added Hare</div>
  <div class="abs" style="left:18px;top:54px;width:86px">
    <p class="tiny" style="font-size:3.5px">Lorem ipsum dolor sit amet, consectetuer ex ea commodo consequat.</p>
    <p class="tiny" style="font-size:3.5px;margin-top:4px">Duis autem vel eum iriure dolor in invulputate velit esse molestie consequat, vel illum dolore eu feugiat nulla facilisis at vero eros et accumsan et iusto odio dignissim qui blandit praesent luptatum zzril delenit augue duis dolore</p>
    <p class="tiny" style="font-size:3.5px;margin-top:4px">Lorem ipsum dolor sit amet, cons ectetueradipiscing elit, sed diam nonummy nibh euismod tincidunt ut laoreet dolore.</p>
  </div>
  <svg class="abs" style="left:122px;top:52px" width="210" height="101" viewBox="0 0 210 101">
    <rect x="0" y="0" width="210" height="101" fill="#fff" stroke="#999" stroke-width=".6"/>
    <rect x="0" y="0" width="210" height="16" fill="#3a3a3b"/>
    <rect x="0" y="0" width="57" height="16" fill="#c4262e"/>
    <g fill="#f3f3f3"><rect x="57" y="33" width="153" height="17"/><rect x="57" y="67" width="153" height="17"/></g>
    <g stroke="#bbb" stroke-width=".4"><line x1="0" y1="33" x2="210" y2="33"/><line x1="0" y1="50" x2="210" y2="50"/><line x1="0" y1="67" x2="210" y2="67"/><line x1="0" y1="84" x2="210" y2="84"/><line x1="57" y1="0" x2="57" y2="101"/><line x1="108" y1="0" x2="108" y2="101"/><line x1="159" y1="0" x2="159" y2="101"/></g>
    <g font-size="3.8" fill="#fff"><text x="8" y="9.5">Text Added Here</text><text x="70" y="9.5">Text One</text><text x="121" y="9.5">Text Two</text><text x="171" y="9.5">Text Three</text></g>
    <g font-size="3.8" fill="#c4262e"><text x="8" y="26">Title Text one</text><text x="8" y="43">Title Text Two</text><text x="8" y="60">Title Text Three</text><text x="8" y="77">Title Text Four</text><text x="8" y="94">Title Text Five</text></g>
  </svg>
  <div class="foot"><span class="brand"><i></i>Torvane</span><b class="rule"></b><span class="pg">12</span></div>
</section>

<!-- 13 Timeline -->
<section class="slide" style="left:54px;top:940px">
  <div class="kicker" style="left:19px;top:15px">Our Company</div>
  <div class="headline" style="left:19px;top:28px">Timeline</div>
  <svg class="abs" style="left:0;top:0" width="348" height="196" viewBox="0 0 348 196">
    <g text-anchor="middle">
      <g font-size="5.4" font-weight="500" fill="#3a3a3b"><text x="65" y="66">Your Title</text><text x="177" y="66">Your Title</text><text x="289" y="66">Your Title</text><text x="121" y="150">Your Title</text><text x="233" y="150">Your Title</text></g>
      <g font-size="3.8" fill="#777"><text x="65" y="71">Refers to a good or</text><text x="65" y="75.5">service being offered</text><text x="177" y="71">Refers to a good or</text><text x="177" y="75.5">service being offered</text><text x="289" y="71">Refers to a good or</text><text x="289" y="75.5">service being offered</text>
        <text x="121" y="155">Refers to a good or</text><text x="121" y="159.5">service being offered</text><text x="233" y="155">Refers to a good or</text><text x="233" y="159.5">service being offered</text></g>
    </g>
    <g stroke="#c4262e" stroke-width=".8"><line x1="65" y1="91" x2="65" y2="105"/><line x1="177" y1="91" x2="177" y2="105"/><line x1="289" y1="91" x2="289" y2="105"/></g>
    <g fill="#c4262e"><circle cx="65" cy="91" r="2"/><circle cx="177" cy="91" r="2"/><circle cx="289" cy="91" r="2"/></g>
    <g stroke="#3a3a3b" stroke-width=".8"><line x1="121" y1="118" x2="121" y2="132"/><line x1="233" y1="118" x2="233" y2="132"/></g>
    <g fill="#3a3a3b"><circle cx="121" cy="132" r="2"/><circle cx="233" cy="132" r="2"/></g>
    <polygon points="42,107 88,107 95,117 35,117" fill="#c4262e"/>
    <polygon points="90,107 149,107 142,117 97,117" fill="#3a3a3b"/>
    <polygon points="151,107 203,107 210,117 144,117" fill="#c4262e"/>
    <polygon points="205,107 264,107 257,117 212,117" fill="#3a3a3b"/>
    <polygon points="266,107 312,107 319,117 259,117" fill="#c4262e"/>
    <g font-size="4.6" font-weight="500" fill="#fff" text-anchor="middle"><text x="65" y="114">1990</text><text x="121" y="114">2001</text><text x="177" y="114">2007</text><text x="233" y="114">2012</text><text x="289" y="114">2020</text></g>
  </svg>
  <div class="foot"><span class="brand"><i></i>Torvane</span><b class="rule"></b><span class="pg">13</span></div>
</section>

<!-- 14 Text and laptop -->
<section class="slide" style="left:425px;top:940px">
  <div class="kicker" style="left:16px;top:17px">Text</div>
  <div class="headline" style="left:16px;top:29px">Added Hare</div>
  <div class="abs" style="left:22px;top:55px;width:112px">
    <p class="tiny" style="font-size:3.6px">Lorem ipsum dolor sit amet consectetuer adipiscing elit, sed diam nonummy nibh euismod tincidunt ut laoreet dolore magna aliquam erat volutpat.Ut wisi enim ad minim veniam</p>
    <p class="tiny" style="font-size:3.6px;margin-top:4px">quis nostrud exerci tation ullamcorper suscipit lobortis nisl ut aliquip ex ea commodo consequat. Lorem ipsum dolor sit amet consectetuer adipiscing elit, sed diam nonummy nibh euismod tincidunt ut laoreet dolore magna aliquam erat volutpat.</p>
    <p class="tiny" style="font-size:3.6px;margin-top:4px">Ut wisi enim ad minim veniam quis nostrud exerci tation ullamcorper suscipit lobortis nisl ut aliquip ex ea commodo consequat.</p>
  </div>
  <div class="abs" style="left:168px;top:52px;width:145px;height:93px;border-radius:4px;background:#1d1d1f"></div>
  <div class="photo" role="img" aria-label="Business team shaking hands around a meeting table" style="left:172px;top:56px;width:137px;height:86px;background:linear-gradient(160deg,#e9eef2 0,#c9d3dc 50%,#8ea2b5 100%)"></div>
  <div class="abs" style="left:153px;top:145px;width:175px;height:5px;border-radius:0 0 6px 6px;background:linear-gradient(#d6d6d8,#9c9ca0)"></div>
  <div class="foot"><span class="brand"><i></i>Torvane</span><b class="rule"></b><span class="pg">14</span></div>
</section>

<!-- 15 Contact -->
<section class="slide" style="left:792px;top:940px">
  <div class="abs" style="left:0;width:348px;top:35px;text-align:center;font-size:16px;font-weight:800;color:var(--red);line-height:1">CONTACT <span style="color:var(--ink)">US</span></div>
  <p class="abs" style="left:60px;width:228px;top:56px;text-align:center;font-size:3.8px;line-height:1.5;color:var(--text)">laoreet dolore magna aliquam erat volutpat. Ut wisi enim ad minim veniam, quis nostrud exerci.aliquam erat volutpat. Ut wisi enim.</p>
  <div class="abs" style="left:25px;top:85px;width:298px;height:54px;border-radius:12px;background:var(--red)"></div>
  <svg class="abs" style="left:0;top:0" width="348" height="196" viewBox="0 0 348 196">
    <circle cx="55" cy="112" r="5" fill="#fff"/><path d="M55 109.5a1.8 1.8 0 1 1 0 3.6 1.8 1.8 0 1 1 0-3.6z" fill="#c4262e"/>
    <circle cx="147" cy="112" r="5" fill="#fff"/><path d="M144.8 109.8c.6 2.3 1.8 3.6 4 4.4l.9-.9-1.2-.9-.6.5c-.8-.4-1.5-1.1-1.9-1.9l.5-.6-.9-1.2z" fill="#c4262e"/>
    <circle cx="227" cy="112" r="5" fill="#fff"/><rect x="224.5" y="110.2" width="5" height="3.6" fill="#c4262e"/><path d="M224.5 110.2l2.5 2 2.5-2" stroke="#fff" stroke-width=".4" fill="none"/>
    <g font-size="4.4" fill="#fff"><text x="66" y="110.5">Address Street Name</text><text x="66" y="116">City Name, Country 000</text>
      <text x="158" y="110.5">(+000) 123 456 789</text><text x="158" y="116">(+000) 123 456 789</text>
      <text x="238" y="110.5">Info@example.com</text><text x="238" y="116">Www.example.com</text></g>
  </svg>
  <div class="abs" style="left:0;width:348px;top:150px;text-align:center;font-size:6px;letter-spacing:2.6px;color:var(--ink)">www.<b style="color:var(--red)">website</b>.com</div>
</section>

</body>
</html>
```